Northern Terrain Published Photographer Website

I need a website to feature a home page slide show of 6 of my top photos then a few simple pages including; gallery, bio, social, checkout, services
Updates

Need extra days to review

Target Market(s)

photography

Industry/Entity Type

Photographer

Coding

Coded - Design and coding required

Number of Pages Required

5+ page

Colors

Designer to choose colors to be used in the design.

Requirements
Must have
• clean eye catching elegant trendy
Nice to have
• unique and creative from other photographer websites

```html
<!DOCTYPE html>
<html lang="en">
<head>
<meta charset="utf-8">
<title>Northern Terrain Photography</title>
<link rel="stylesheet" href="https://fonts.googleapis.com/css2?family=Lato:wght@400;700&family=Yellowtail&display=swap">
<style>
:root{
  --ink:#000000;
  --paper:#ffffff;
  --muted:#d9d9d9;
  --rule:#3a3a3a;
  --script:"Yellowtail", cursive;
  --body:"Lato", sans-serif;
}
*{margin:0;padding:0;box-sizing:border-box}
html,body{width:1200px;height:3523px;overflow:hidden;background:var(--ink)}
body{position:relative;font-family:var(--body);color:var(--paper)}
.abs{position:absolute}
.center{left:0;width:1200px;text-align:center}
.script{font-family:var(--script);font-weight:400}
.btn{position:absolute;border:2px solid var(--paper);color:var(--paper);font-size:16px;display:flex;align-items:center;justify-content:center;font-family:var(--body)}
.photo{position:absolute}

/* header */
.site-header{left:0;top:0;width:1200px;height:92px;background:var(--ink)}
.brand{display:flex;align-items:center;gap:10px;font-family:var(--body);font-size:24px;font-weight:400;color:var(--paper);letter-spacing:1px}
.brand-dot{width:14px;height:14px;border-radius:50%;background:var(--paper)}

/* hero */
.hero{left:0;top:92px;width:1200px;height:569px;
  background:linear-gradient(180deg,#6f6f8c 0%,#a99aa0 18%,#8a8aa8 32%,#5b5e86 48%,#3c3f6e 62%,#2a2c52 78%,#1d1d2c 100%)}
.hero-title{top:322px;font-size:32px;line-height:41px}
.dots{left:576px;top:606px;display:flex;gap:7px}
.dots span{width:6px;height:6px;border-radius:50%;background:#8a8a9a}
.dots span.on{background:var(--paper)}

/* services */
.section-title{font-size:32px}
.service{position:absolute;width:270px;text-align:center}
.service .disc{width:234px;height:234px;border-radius:50%;margin:0 auto}
.service h3{font-family:var(--script);font-weight:400;font-size:17px;margin-top:24px}
.service p{font-size:14px;line-height:24px;margin-top:17px}

/* gallery */
.tile{position:absolute;width:327px;height:328px}

/* about */
.about-text{left:72px;width:380px;text-align:center;font-size:16px;line-height:24px}
.frame-top{border:8px solid var(--ink)}

/* instagram */
.insta{position:absolute;top:2862px;width:245px;height:237px}

/* footer */
.social{left:521px;top:3213px;display:flex;gap:10px}
.social span{width:24px;height:24px;border-radius:50%;border:2px solid var(--paper)}
.contact{font-size:15px;display:flex;align-items:center;gap:12px}
.contact .ic{width:30px;height:30px;border-radius:50%;background:var(--paper);display:flex;align-items:center;justify-content:center}
.field{position:absolute;border:2px solid var(--paper);font-size:14px;display:flex;align-items:center}
.foot-nav{left:0;width:1200px;top:3432px;display:flex;justify-content:center;gap:44px;font-family:var(--script);font-size:14px}
.rule{left:0;top:3472px;width:1200px;height:1px;background:var(--rule)}
.copy{top:3487px;font-size:14px}
</style>
</head>
<body>

<header class="abs site-header">
  <svg class="abs" style="left:80px;top:35px" width="18" height="14" viewBox="0 0 18 14"><rect y="0" width="18" height="2.4" fill="#fff"/><rect y="5.8" width="18" height="2.4" fill="#fff"/><rect y="11.6" width="18" height="2.4" fill="#fff"/></svg>
  <div class="abs center" style="top:26px;display:flex;justify-content:center"><div class="brand"><span>Northern Terrain</span><span class="brand-dot"></span></div></div>
  <svg class="abs" style="left:970px;top:38px" width="16" height="16" viewBox="0 0 16 16" fill="none" stroke="#fff" stroke-width="1.6"><circle cx="6.5" cy="6.5" r="5"/><path d="M10.5 10.5 15 15"/></svg>
  <svg class="abs" style="left:1019px;top:37px" width="16" height="17" viewBox="0 0 16 17" fill="none" stroke="#fff" stroke-width="1.6"><circle cx="8" cy="5" r="4"/><path d="M1 16c0-4 3-6 7-6s7 2 7 6"/></svg>
  <svg class="abs" style="left:1062px;top:38px" width="18" height="16" viewBox="0 0 18 16" fill="none" stroke="#fff" stroke-width="1.6"><path d="M9 15 2 8a4 4 0 0 1 7-5 4 4 0 0 1 7 5z"/></svg>
  <svg class="abs" style="left:1103px;top:32px" width="22" height="22" viewBox="0 0 22 22" fill="none" stroke="#fff" stroke-width="1.6"><path d="M1 6h3l2 9h10l2-7H5"/><circle cx="8" cy="19" r="1.5"/><circle cx="15" cy="19" r="1.5"/><circle cx="17" cy="5" r="4" fill="#000"/><text x="17" y="7.5" font-size="6" fill="#fff" stroke="none" text-anchor="middle" font-family="Lato, sans-serif">0</text></svg>
</header>

<section class="abs hero" role="img" aria-label="Snow-capped mountain range under a soft dusk sky"></section>
<h1 class="abs center script hero-title">Seeing The World, Through the<br>Eyes of My Lens</h1>
<a class="btn" style="left:512px;top:430px;width:173px;height:47px;color:#cfcfcf">Read More</a>
<div class="abs dots"><span class="on"></span><span></span><span></span><span></span></div>
<svg class="abs" style="left:1058px;top:600px" width="66" height="16" viewBox="0 0 66 16" fill="none" stroke="#fff" stroke-width="1.6"><path d="M26 8H2M8 2 2 8l6 6"/><path d="M40 8h24M58 2l6 6-6 6"/></svg>

<h2 class="abs center script section-title" style="top:714px">Our Services</h2>
<div class="service" style="left:63px;top:780px"><div class="disc" role="img" aria-label="Green hills under a cloudy sky" style="background:radial-gradient(circle at 50% 25%,#b8c2cc,#6d8a4a 55%,#4f6e2c)"></div><h3>Geographic Nature</h3><p>Lorem Ipsum is simply dummy<br>of the printing and typesetting<br>io the industry.</p></div>
<div class="service" style="left:333px;top:780px"><div class="disc" role="img" aria-label="Wild sheep on a rocky slope" style="background:linear-gradient(180deg,#7fb3e0 0%,#b58a78 35%,#9c8572 70%,#6f6257)"></div><h3>Wildlife</h3><p>Lorem Ipsum is simply dummy<br>of the printing and typesetting<br>io the industry.</p></div>
<div class="service" style="left:602px;top:780px"><div class="disc" role="img" aria-label="Canyon bend with a green river" style="background:radial-gradient(circle at 50% 55%,#8a5a44 0%,#2f5a4a 40%,#7a5040 75%,#4a3a34)"></div><h3>Landscape,</h3><p>Lorem Ipsum is simply dummy<br>of the printing and typesetting<br>io the industry.</p></div>
<div class="service" style="left:872px;top:780px"><div class="disc" role="img" aria-label="Orange sunset over a pier" style="background:radial-gradient(circle at 50% 40%,#fff3a0 0%,#f7b21f 25%,#e6761a 55%,#7a2e0a 100%)"></div><h3>Sunsets/Sunrises</h3><p>Lorem Ipsum is simply dummy<br>of the printing and typesetting<br>io the industry.</p></div>
<a class="btn" style="left:513px;top:1200px;width:174px;height:49px">View More</a>

<h2 class="abs center script section-title" style="top:1293px">Gallery</h2>
<div class="tile" style="left:81px;top:1368px" role="img" aria-label="Desert butte under storm clouds" style="background:#333"></div>
<div class="tile" style="left:81px;top:1368px;background:linear-gradient(180deg,#2b2f2f 0%,#3f4a3d 40%,#8a5424 60%,#3a2414 100%)" role="img" aria-label="Desert butte under storm clouds"></div>
<div class="tile" style="left:438px;top:1368px;background:linear-gradient(180deg,#dcdcdc 0%,#8d939a 35%,#4d7f88 60%,#c9a888 100%)" role="img" aria-label="Lake among sandstone under clouds"></div>
<div class="tile" style="left:795px;top:1368px;background:linear-gradient(180deg,#2f6fd6 0%,#4f8ad8 25%,#c06a3a 45%,#f3b040 55%,#c89a78 80%,#e0c2a8 100%)" role="img" aria-label="Sunburst under a rock arch"></div>
<div class="tile" style="left:81px;top:1724px;background:linear-gradient(180deg,#6dc3c0 0%,#e0a040 30%,#c07a2a 52%,#6fa0a0 56%,#d09a50 80%,#6aa6a4 100%)" role="img" aria-label="Sandstone tower reflected in a lake"></div>
<div class="tile" style="left:438px;top:1724px;background:linear-gradient(180deg,#7a3a8a 0%,#e0507a 35%,#ffb070 50%,#c03a6a 70%,#5a2a6a 100%)" role="img" aria-label="Joshua tree against a vivid sunset"></div>
<div class="tile" style="left:795px;top:1724px;background:linear-gradient(180deg,#7a6ad0 0%,#e08a70 25%,#6a5ab8 45%,#7a6ac0 100%)" role="img" aria-label="Glass sphere on a beach at dusk"></div>
<a class="btn" style="left:513px;top:2085px;width:174px;height:49px">View More</a>

<h2 class="abs script" style="left:72px;width:380px;text-align:center;top:2318px;font-size:30px">About us</h2>
<p class="abs about-text" style="top:2371px">Lorem Ipsum is simply dummy text of the printing and typesetting industry.</p>
<p class="abs about-text" style="top:2443px">Lorem Ipsum has been the industry's standard on dummy text ever since the 1500s, when an known printer took a galley of type and scrambled it to make a type specimen book.</p>
<a class="btn" style="left:176px;top:2568px;width:174px;height:49px">Read More</a>
<div class="photo" style="left:651px;top:2315px;width:468px;height:345px;background:linear-gradient(180deg,#f3f3f5 0%,#8fb5d8 28%,#3f7ab0 40%,#7a6e66 60%,#c8c0b6 100%)" role="img" aria-label="Person walking a small dog along a wooden pier"></div>
<div class="photo frame-top" style="left:476px;top:2220px;width:297px;height:367px;background:linear-gradient(180deg,#eef0f2 0%,#e8dccb 35%,#9a9aa0 75%,#7d7e84 100%)" role="img" aria-label="Portrait of the photographer"></div>

<h2 class="abs center script" style="top:2733px;font-size:30px">Follow Us On Instagram</h2>
<p class="abs center script" style="top:2776px;font-size:15px">Lorem Ipsum is simply dummy text of the printing.</p>
<div class="insta" style="left:81px;background:linear-gradient(180deg,#3a7ad0 0%,#a8c0e0 40%,#a0502a 70%,#6a4a3a 100%)" role="img" aria-label="Stacked rock cairn with sunburst"></div>
<div class="insta" style="left:346px;background:linear-gradient(180deg,#8a7aa0 0%,#c2a0a8 35%,#8a6a54 60%,#b08a6a 100%)" role="img" aria-label="Eroded desert badlands at dusk"></div>
<div class="insta" style="left:610px;background:radial-gradient(circle at 50% 55%,#e0e0d8 0%,#5a7a3a 30%,#8a8a5a 60%,#3a4a2a 100%)" role="img" aria-label="Waterfall seen through a fisheye lens"></div>
<div class="insta" style="left:876px;background:linear-gradient(180deg,#d0402a 0%,#f0702a 40%,#e0502a 65%,#5a1a10 100%)" role="img" aria-label="Red sunset over a pier"></div>

<div class="abs center" style="top:3158px;display:flex;justify-content:center"><div class="brand"><span>Northern Terrain</span><span class="brand-dot"></span></div></div>
<div class="abs social"><span></span><span></span><span></span><span></span><span></span></div>

<div class="abs contact" style="left:281px;top:3258px"><span class="ic"><svg width="16" height="16" viewBox="0 0 16 16"><path d="M3 1 6 4 4.5 6c1 2 3 4 5.5 5.5L12 10l3 3-2 2C7 14 2 9 1 3z" fill="#000"/></svg></span>123. 456.7890</div>
<div class="abs contact" style="left:468px;top:3258px;font-weight:700"><span class="ic"><svg width="14" height="18" viewBox="0 0 14 18"><path d="M7 17S1 10 1 6.5a6 6 0 0 1 12 0C13 10 7 17 7 17z" fill="#000"/><circle cx="7" cy="6.5" r="2.2" fill="#fff"/></svg></span>123 Streel, City Country,</div>
<div class="abs" style="left:565px;top:3295px;font-size:15px;font-weight:700">Zip Code</div>
<div class="abs contact" style="left:727px;top:3256px;font-size:14px"><span class="ic"><svg width="16" height="12" viewBox="0 0 16 12" fill="none" stroke="#000" stroke-width="1.6"><rect x="1" y="1" width="14" height="10"/><path d="m1 1 7 6 7-6"/></svg></span>info@northernterrain.com</div>

<h2 class="abs center script" style="top:3325px;font-size:24px">Join Our Newletter</h2>
<div class="field" style="left:408px;top:3367px;width:292px;height:28px;padding-left:14px">Email</div>
<div class="field" style="left:711px;top:3367px;width:85px;height:28px;justify-content:center">Submit</div>

<nav class="abs foot-nav"><span>Home</span><span>.</span><span>Bio</span><span>.</span><span>Gallery</span><span>.</span><span>Social</span><span>.</span><span>Checkout</span><span>.</span><span>Services</span></nav>
<div class="abs rule"></div>
<p class="abs center copy">Copyright © 2019 Northern Terrain. All Rights Reserved.</p>

</body>
</html>
```